Bag Design For Frozen Prawns

Basically we need a design for a plastic bag that we have packed in Vietnam. I have attached a copy of our logo a picture of a bag I like.
As you can see it is simple clean and fresh.

Target Market(s)

Chefs

Industry/Entity Type

Plastic

```html
<!DOCTYPE html>
<html lang="en">
<head>
<meta charset="utf-8">
<title>Tideharbor Raw Shrimp Bag</title>
<link rel="stylesheet" href="https://fonts.googleapis.com/css2?family=Archivo+Black&family=Archivo+Narrow:wght@700&display=swap">
<style>
  :root {
    --navy: #2a2e86;
    --brand-blue: #1e7fc4;
    --water-light: #d6eefb;
    --water-mid: #7cc4ec;
    --water-deep: #2f8fd0;
    --leaf: #9ccc3c;
    --leaf-dark: #1f3b10;
    --white: #ffffff;
    --shrimp-light: #c9d2c4;
    --shrimp-mid: #8ea291;
    --shrimp-dark: #5f7364;
    --cream: #f3e4d4;
    --coral: #d9a184;
  }
  * { margin: 0; padding: 0; box-sizing: border-box; }
  html, body { width: 750px; height: 1200px; overflow: hidden; background: var(--white); }
  .bag {
    position: relative;
    width: 750px;
    height: 1200px;
    background: var(--white);
    overflow: hidden;
    font-family: "Archivo Black", "Arial Black", sans-serif;
  }
  .water-splash {
    position: absolute;
    left: 0; top: 0;
    width: 750px; height: 420px;
    background:
      radial-gradient(ellipse 60% 45% at 70% 40%, var(--water-mid) 0%, rgba(124,196,236,0) 70%),
      radial-gradient(ellipse 50% 40% at 15% 75%, var(--water-deep) 0%, rgba(47,143,208,0) 70%),
      linear-gradient(180deg, var(--white) 0%, var(--water-light) 55%, var(--white) 100%);
  }
  .brand {
    position: absolute;
    left: 40px; top: 22px;
    display: flex; align-items: center; gap: 16px;
  }
  .brand-dot {
    width: 64px; height: 64px; border-radius: 50%;
    background: var(--brand-blue);
  }
  .brand-name {
    font-size: 62px;
    color: var(--brand-blue);
    letter-spacing: 1px;
    line-height: 1;
  }
  .product-oval {
    position: absolute;
    left: 50px; top: 160px;
    width: 330px; height: 150px;
    border-radius: 50%;
    background: var(--navy);
    border: 5px solid var(--white);
    color: var(--white);
    text-align: center;
  }
  .product-name {
    display: block;
    margin-top: 20px;
    font-size: 62px;
    line-height: 1;
  }
  .product-state {
    display: flex; align-items: center; justify-content: center; gap: 14px;
    margin-top: 6px;
    font-size: 28px;
    letter-spacing: 2px;
  }
  .product-state::before, .product-state::after {
    content: ""; width: 46px; height: 3px; background: var(--white);
  }
  .shrimp-art {
    position: absolute;
    left: 400px; top: 95px;
    width: 330px; height: 255px;
    border-radius: 40% 50% 45% 55%;
    background: radial-gradient(ellipse at 45% 45%, var(--cream) 0%, var(--coral) 60%, rgba(217,161,132,0) 100%);
  }
  .prep-banner {
    position: absolute;
    left: 25px; top: 330px;
    width: 455px; height: 46px;
    background: var(--leaf);
    border-radius: 23px;
    color: var(--leaf-dark);
    font-family: "Archivo Narrow", "Arial Narrow", sans-serif;
    font-weight: 700;
    font-size: 27px;
    line-height: 46px;
    text-align: center;
    letter-spacing: 0.5px;
  }
  .window-frame {
    position: absolute;
    left: 18px; top: 400px;
    width: 714px; height: 775px;
    background: var(--navy);
    padding: 38px 38px;
  }
  .product-photo {
    width: 100%; height: 100%;
    background:
      repeating-linear-gradient(90deg, var(--shrimp-light) 0 40px, var(--shrimp-mid) 40px 60px, var(--shrimp-dark) 60px 64px),
      var(--shrimp-mid);
    opacity: 0.95;
  }
  .count-badge {
    position: absolute;
    left: 520px; top: 905px;
    width: 210px; height: 210px;
  }
  .count-badge svg { position: absolute; inset: 0; }
  .count-text {
    position: absolute; inset: 0;
    display: flex; flex-direction: column; align-items: center; justify-content: center;
    color: var(--leaf-dark);
    text-align: center;
  }
  .count-range { font-size: 52px; line-height: 1; }
  .count-unit {
    font-family: "Archivo Narrow", "Arial Narrow", sans-serif;
    font-weight: 700;
    font-size: 15px;
    margin-top: 6px;
  }
</style>
</head>
<body>
  <main class="bag">
    <div class="water-splash" role="img" aria-label="Splash of clear blue water"></div>

    <header class="brand">
      <span class="brand-dot"></span>
      <span class="brand-name">TIDEHARBOR</span>
    </header>

    <div class="product-oval">
      <span class="product-name">SHRIMP</span>
      <span class="product-state">RAW</span>
    </div>

    <div class="shrimp-art" role="img" aria-label="Two raw shrimp with tails"></div>

    <div class="prep-banner">PEELED, DEVIENED, TAIL-ON</div>

    <section class="window-frame">
      <div class="product-photo" role="img" aria-label="Rows of raw peeled shrimp seen through the bag window"></div>
    </section>

    <div class="count-badge">
      <svg viewBox="0 0 210 210" aria-hidden="true">
        <polygon fill="#9ccc3c" points="105,2 121,22 145,10 152,35 178,32 176,58 201,66 188,89 208,105 188,121 201,144 176,152 178,178 152,175 145,200 121,188 105,208 89,188 65,200 58,175 32,178 34,152 9,144 22,121 2,105 22,89 9,66 34,58 32,32 58,35 65,10 89,22"/>
      </svg>
      <div class="count-text">
        <span class="count-range">35-45</span>
        <span class="count-unit">SHRIMP SPER POUND</span>
      </div>
    </div>
  </main>
</body>
</html>
```